New Business Card Design Project

Harbor of the Willow Wellness Clinic PLLC
Harborofthewillowwc.example
Board Certified Nursing Coach in life, health, & wellness.
Hypnotherapy, weight loss & vitamin supplement injections, IV hydration.
Offering mobile clinics

```html
<!DOCTYPE html>
<html lang="en">
<head>
<meta charset="utf-8">
<title>Harbor of the Willow Wellness Clinic – Business Card</title>
<link rel="stylesheet" href="https://fonts.googleapis.com/css2?family=Montserrat:wght@500;600;700&family=Roboto:wght@400;500;700&display=swap">
<style>
  :root {
    --stage: #202020;
    --card-black: #161616;
    --card-black-soft: #262626;
    --orange: #e8521f;
    --orange-light: #f7b46c;
    --gold: #e9b46a;
    --tan: #b89676;
    --white: #f4f1ee;
  }
  * { box-sizing: border-box; margin: 0; padding: 0; }
  html, body {
    width: 1200px; height: 801px; overflow: hidden;
    background: var(--stage);
  }
  .canvas {
    position: relative; width: 1200px; height: 801px;
    display: flex; align-items: center; justify-content: center; gap: 40px;
  }
  .card {
    position: relative; width: 540px; height: 308px;
    border-radius: 16px; overflow: hidden;
    background: linear-gradient(135deg, var(--card-black-soft), var(--card-black) 60%);
    box-shadow: 0 18px 40px rgba(0,0,0,.55);
  }
  .card-front__art { position: absolute; inset: 0; width: 100%; height: 100%; }
  .brand-mark {
    position: absolute; left: 34px; top: 128px;
    display: flex; align-items: center; gap: 12px;
  }
  .brand-mark__dot {
    flex: 0 0 34px; height: 34px; border-radius: 50%;
    background: var(--orange);
  }
  .brand-mark__name {
    font-family: 'Montserrat', sans-serif; font-weight: 600;
    font-size: 17px; line-height: 1.25; color: var(--gold); white-space: nowrap;
  }
  .holder {
    position: absolute; right: 30px; top: 20px; text-align: right;
    font-family: 'Roboto', sans-serif; color: var(--white);
  }
  .holder__name { color: var(--orange); font-weight: 700; font-size: 22px; letter-spacing: .5px; line-height: 1.2; }
  .holder__name span { color: var(--gold); }
  .holder__title { font-size: 15px; margin-top: 1px; }
  .holder__address { font-size: 13px; margin-top: 10px; line-height: 1.35; }
  .contact {
    position: absolute; right: 22px; top: 150px; list-style: none;
    font-family: 'Roboto', sans-serif; font-size: 13px; color: var(--white);
  }
  .contact li { display: flex; align-items: center; justify-content: flex-end; gap: 8px; height: 21px; }
  .contact svg { width: 12px; height: 12px; fill: var(--white); }

  .card-back { padding: 30px 40px 0 200px; }
  .card-back__brand {
    font-family: 'Montserrat', sans-serif; font-weight: 600; font-size: 19px;
    color: var(--gold); text-align: center; line-height: 1.25;
  }
  .card-back__rule {
    height: 1px; margin: 10px auto 0; width: 80%;
    background: linear-gradient(90deg, transparent, var(--gold), transparent);
  }
  .services { margin-top: 14px; font-family: 'Montserrat', sans-serif; color: var(--white); }
  .services__title {
    font-weight: 700; font-size: 22px; letter-spacing: .5px;
    background: linear-gradient(90deg, var(--orange), var(--gold));
    -webkit-background-clip: text; background-clip: text; color: transparent;
  }
  .services__list { list-style: none; margin-top: 6px; font-size: 13px; font-weight: 500; line-height: 1.38; }
  .services__list li { position: relative; padding-left: 16px; }
  .services__list li::before {
    content: ""; position: absolute; left: 0; top: 6px;
    width: 7px; height: 7px; border-radius: 50%; background: var(--orange-light);
  }
</style>
</head>
<body>
<main class="canvas">
  <section class="card card-front">
    <svg class="card-front__art" viewBox="0 0 540 308" preserveAspectRatio="none" aria-hidden="true">
      <defs>
        <linearGradient id="panelGlow" x1="1" y1="0" x2="0" y2="1">
          <stop offset="0" stop-color="#e8521f"/>
          <stop offset="1" stop-color="#f9c283"/>
        </linearGradient>
      </defs>
      <path d="M-10 270 C120 280 230 268 330 212" fill="none" stroke="#e8521f" stroke-width="10"/>
      <path d="M-10 294 C130 306 250 292 350 236" fill="none" stroke="#f7b46c" stroke-width="8"/>
      <path d="M540 128 C400 124 330 140 295 190 C260 240 190 292 40 308 L540 308 Z" fill="url(#panelGlow)"/>
      <path d="M540 117 C395 113 320 130 284 182 C248 234 178 284 10 304" fill="none" stroke="#b89676" stroke-width="5"/>
    </svg>
    <div class="brand-mark">
      <span class="brand-mark__dot"></span>
      <span class="brand-mark__name">Harbor of the Willow</span>
    </div>
    <div class="holder">
      <p class="holder__name">DANIEL <span>MARSH</span></p>
      <p class="holder__title">Managing Director</p>
      <p class="holder__address">Your Address, City<br>State, Zip 0000</p>
    </div>
    <ul class="contact">
      <li>044-987 654 321
        <svg viewBox="0 0 24 24"><path d="M6.6 10.8a15 15 0 0 0 6.6 6.6l2.2-2.2a1 1 0 0 1 1-.25 11.4 11.4 0 0 0 3.6.57 1 1 0 0 1 1 1V20a1 1 0 0 1-1 1A17 17 0 0 1 3 4a1 1 0 0 1 1-1h3.5a1 1 0 0 1 1 1c0 1.25.2 2.45.57 3.57a1 1 0 0 1-.25 1z"/></svg></li>
      <li>info@harborwillow.example
        <svg viewBox="0 0 24 24"><path d="M2 5h20v14H2zm2 2v.5l8 5 8-5V7l-8 5z"/></svg></li>
      <li>Harborofthewillowwc.example
        <svg viewBox="0 0 24 24"><circle cx="12" cy="12" r="10"/></svg></li>
    </ul>
  </section>

  <section class="card card-back">
    <p class="card-back__brand">Harbor of the Willow<br>Wellness Clinic</p>
    <div class="card-back__rule"></div>
    <div class="services">
      <h2 class="services__title">OUR SERVICE</h2>
      <ul class="services__list">
        <li>Board Certified Nursing Coach in life health &amp; wellness.</li>
        <li>Hypnotherapy</li>
        <li>weight loss</li>
        <li>vitamin supplement injections</li>
        <li>IV hydration</li>
        <li>Offering mobile clinics</li>
      </ul>
    </div>
  </section>
</main>
</body>
</html>
```